Enlargement project

We would like to create an enlargement of the attached business card design, so that we are able to print hi-res business cards from it,

The end result we are after is an illustrator template that contains hi-res graphics and text that we can edit to insert people's names, job titles, phone and email details

The two colours used within the design are:

Pantone 350 (green)
Panton 484 (red)

The fonts used are;

Futura Medium
Futura Bk BT Italic

```html
<!DOCTYPE html>
<html lang="en">
<head>
<meta charset="utf-8">
<title>Sentinel business card</title>
<link rel="stylesheet" href="https://fonts.googleapis.com/css2?family=Arimo:wght@400;700&display=swap">
<style>
  :root {
    --brand-red: #b5161b;
    --ink: #111111;
    --paper: #ffffff;
    --rule-grey: #d9d9db;
    --frame-grey: #d0d0d0;
    --pattern-top: #cfcfd1;
    --pattern-bottom: #f6f6f6;
    --accent-black: #000000;
  }
  * { margin: 0; padding: 0; box-sizing: border-box; }
  html, body {
    width: 1200px; height: 349px; overflow: hidden;
    background: var(--paper);
    font-family: "Arimo", Arial, sans-serif;
  }
  .canvas { position: relative; width: 1200px; height: 349px; }

  .card { position: absolute; top: 12px; height: 324px; overflow: hidden; }

  /* Front */
  .card-front { left: 12px; width: 528px; }
  .front-pattern {
    position: absolute; inset: 0 0 12px 0;
    background: linear-gradient(180deg, var(--pattern-top) 0%, var(--pattern-bottom) 100%);
  }
  .front-stripe {
    position: absolute; left: 0; right: 0; bottom: 0; height: 12px;
    background: var(--brand-red);
  }
  .front-stripe-end {
    position: absolute; right: 0; bottom: 0; width: 34px; height: 12px;
    background: var(--accent-black);
  }
  .front-brand {
    position: absolute; left: 96px; top: 118px;
    display: flex; align-items: center; gap: 14px;
  }

  .brand-name {
    font-weight: 700; color: var(--ink); letter-spacing: -0.5px; line-height: 1;
  }
  .brand-square { background: var(--brand-red); flex: none; }
  .front-brand .brand-name { font-size: 58px; }
  .front-brand .brand-square { width: 118px; height: 118px; }

  /* Back */
  .card-back {
    left: 662px; width: 526px;
    background: var(--paper);
    border: 1px solid var(--frame-grey);
  }
  .back-brand {
    position: absolute; left: 0; right: 0; top: 42px;
    display: flex; justify-content: center; align-items: center; gap: 10px;
  }
  .back-brand .brand-name { font-size: 36px; }
  .back-brand .brand-square { width: 74px; height: 74px; }

  .person {
    position: absolute; left: 0; right: 0; top: 144px; text-align: center;
  }
  .person-name { font-weight: 700; font-size: 23px; color: var(--ink); line-height: 1.15; }
  .person-role { font-size: 23px; color: var(--brand-red); line-height: 1.2; }

  .back-rule {
    position: absolute; left: 0; right: 0; top: 218px; height: 9px;
    background: var(--rule-grey);
  }
  .back-band {
    position: absolute; left: 0; right: 0; top: 227px; bottom: 0;
    background: var(--brand-red); color: var(--paper);
  }
  .website {
    position: absolute; left: 39px; top: 50px;
    font-weight: 700; font-size: 22px;
  }
  .contact-list {
    position: absolute; left: 338px; top: 14px;
    list-style: none; font-size: 18px; line-height: 26px;
  }
</style>
</head>
<body>
<div class="canvas">

  <section class="card card-front" aria-label="Card front">
    <div class="front-pattern" role="img" aria-label="Repeating pale grey letter pattern background"></div>
    <div class="front-stripe"></div>
    <div class="front-stripe-end"></div>
    <div class="front-brand">
      <span class="brand-name">Sentinel</span>
      <span class="brand-square"></span>
    </div>
  </section>

  <section class="card card-back" aria-label="Card back">
    <div class="back-brand">
      <span class="brand-name">Sentinel</span>
      <span class="brand-square"></span>
    </div>
    <div class="person">
      <p class="person-name">Morgan</p>
      <p class="person-role">Technical Operations</p>
    </div>
    <div class="back-rule"></div>
    <div class="back-band">
      <p class="website">www.sentinel-ops.net</p>
      <ul class="contact-list">
        <li>T 02 5550</li>
        <li>F 02 5550</li>
        <li>D 02 55 50</li>
      </ul>
    </div>
  </section>

</div>
</body>
</html>
```